Brambury Logistics

Create a modern, simple, Elegant business card design for my business.

Services: Tamo Trucks, Transport, Contract Logistics,

Industry/Entity Type

Business

Contact Information for Business Card

Include all details same as old card plus new website address: www.bramburylogistics.com.au

Requirements
Must have
• Similar colors to Logo.

```html
<!DOCTYPE html>
<html lang="en">
<head>
<meta charset="utf-8">
<title>Brambury Logistics – Business Card</title>
<link href="https://fonts.googleapis.com/css2?family=Lato:wght@400;700&display=swap" rel="stylesheet">
<style>
  :root {
    --backdrop: #3b3b3b;
    --brand-blue-dark: #124a78;
    --brand-blue: #0d69a0;
    --paper: #ffffff;
    --arc-grey: #85888c;
    --logo-grey: #6d7075;
    --text-light: #ffffff;
  }
  * { box-sizing: border-box; margin: 0; padding: 0; }
  html, body { width: 1200px; height: 810px; overflow: hidden; }
  body {
    background: var(--backdrop);
    font-family: "Lato", sans-serif;
    position: relative;
  }
  .card {
    position: absolute;
    left: 290px;
    width: 620px;
    height: 354px;
    overflow: hidden;
    box-shadow: 0 6px 18px rgba(0,0,0,.35);
  }
  .card--front {
    top: 36px;
    background: linear-gradient(160deg, var(--brand-blue-dark) 0%, var(--brand-blue) 100%);
    color: var(--text-light);
    text-align: center;
  }
  .front__name {
    position: absolute;
    top: 118px;
    left: 0; right: 0;
    font-size: 44px;
    font-weight: 700;
    letter-spacing: .5px;
    color: var(--text-light);
  }
  .front__services {
    position: absolute;
    top: 226px;
    left: 0; right: 0;
    font-size: 15px;
    line-height: 1.55;
  }
  .card--back { top: 420px; background: var(--paper); }
  .back__shape { position: absolute; inset: 0; }
  .back__name {
    position: absolute;
    left: 24px;
    width: 240px;
    top: 160px;
    text-align: center;
    font-size: 26px;
    font-weight: 700;
    white-space: nowrap;
    color: var(--logo-grey);
  }
  .back__contact {
    position: absolute;
    left: 392px;
    top: 96px;
    color: var(--text-light);
  }
  .contact__person { font-size: 22px; font-weight: 400; }
  .contact__role { font-size: 14px; margin-bottom: 16px; }
  .contact__list { list-style: none; font-size: 13px; }
  .contact__list li { display: flex; align-items: center; gap: 8px; margin-bottom: 6px; white-space: nowrap; }
  .contact__list svg { width: 13px; height: 13px; fill: var(--text-light); flex: none; }
</style>
</head>
<body>
  <section class="card card--front">
    <div class="front__name">Brambury Logistics</div>
    <p class="front__services">Services:<br>Tamo Trucks, Transport, Contract Logistics</p>
  </section>

  <section class="card card--back">
    <svg class="back__shape" viewBox="0 0 620 354" preserveAspectRatio="none" aria-hidden="true">
      <defs>
        <linearGradient id="panelBlue" x1="0" y1="0" x2="0.6" y2="1">
          <stop offset="0" stop-color="#124a78"/>
          <stop offset="1" stop-color="#0d69a0"/>
        </linearGradient>
      </defs>
      <path d="M318 0 Q236 200 392 354" fill="none" stroke="#85888c" stroke-width="7"/>
      <path d="M332 0 Q252 200 408 354 L620 354 L620 0 Z" fill="url(#panelBlue)"/>
    </svg>
    <div class="back__name">Brambury Logistics</div>
    <div class="back__contact">
      <div class="contact__person">Adrian Kellow</div>
      <div class="contact__role">President</div>
      <ul class="contact__list">
        <li><svg viewBox="0 0 24 24"><path d="M6.6 10.8a15 15 0 0 0 6.6 6.6l2.2-2.2a1 1 0 0 1 1-.25 11.4 11.4 0 0 0 3.6.57 1 1 0 0 1 1 1V20a1 1 0 0 1-1 1A17 17 0 0 1 3 4a1 1 0 0 1 1-1h3.5a1 1 0 0 1 1 1c0 1.250.2 2.45.57 3.57a1 1 0 0 1-.25 1z"/></svg>0412 555 308</li>
        <li><svg viewBox="0 0 24 24"><path d="M2 5h20v14H2z M2 5l10 8 10-8" fill="none" stroke="#fff" stroke-width="2"/></svg>adrian@bramburylogistics.com.au</li>
        <li><svg viewBox="0 0 24 24"><circle cx="12" cy="12" r="9" fill="none" stroke="#fff" stroke-width="2"/><path d="M3 12h18M12 3c3 3 3 15 0 18M12 3c-3 3-3 15 0 18" fill="none" stroke="#fff" stroke-width="1.6"/></svg>www.bramburylogistics.com.au</li>
      </ul>
    </div>
  </section>
</body>
</html>
```